Lena Business card

This card is to represent me as a coach and Vivamora facilitator
Double sided in colour
A beautiful, simple and elegant design that indicates movement and is modern, FRESH and uplifting. Please don’t use much black and use the attached Vivamora logo.
Preferred colours - white, lighter blues and fresh greens

Target Market(s)
Business people - potential clients age 35 up
Industry/Entity Type
Business
Requirements
Must have
-  Text for the front :
Lumivera Living
Lena Darrow
Biocentric Coach
Co-Director, Vivamora School of Australia
E: lena@vivamora.com.au
M: 0471 552 908.
W: vivamora.com.au
Biocentric Coaching for Individuals, Teams and Organisations
Vivamora for Children, Adults and Social development projects
Text for the back :
The Vivamora system facilitates the expression of human potential for health, happiness and humanity through music, movement and group interaction. It was developed by Emilio Vasca Orduña, a Chilean anthropologist and clinical psychologist, in 1976.
Creative use of the logo - integrating it within the design - e.g perhaps using it as the O in Vivamora,
Please feature the heron from the logo or a another elegant graceful stylized heron.

```html
<!DOCTYPE html>
<html lang="en">
<head>
<meta charset="utf-8">
<title>Lena Darrow – Business Card</title>
<link rel="stylesheet" href="https://fonts.googleapis.com/css2?family=Saira+Extra+Condensed:wght@400;500&display=swap">
<style>
  :root {
    --page: #ece8e2;
    --card-white: #f7f7f5;
    --blue: #1eaed6;
    --blue-back: #27b2d9;
    --green: #6abf3b;
    --ink-blue: #2e62ae;
    --white: #ffffff;
  }
  * { margin: 0; padding: 0; box-sizing: border-box; }
  html, body { width: 1200px; height: 1000px; overflow: hidden; background: var(--page); }
  .scene { display: block; width: 1200px; height: 1000px; }
  .scene text {
    font-family: "Saira Extra Condensed", "Arial Narrow", sans-serif;
    text-transform: uppercase;
  }
  .card-front-face { fill: var(--card-white); }
  .card-back-face { fill: var(--blue-back); }
  .tile-face { fill: var(--blue); }
  .mark-ring-blue { fill: none; stroke: var(--blue); stroke-width: 1.5; stroke-dasharray: 4 3; }
  .mark-ring-white { fill: none; stroke: var(--white); stroke-width: 2; }
  .mark-name-blue { fill: var(--blue); font-weight: 500; }
  .mark-name-white { fill: var(--white); font-weight: 500; }
  .t-blue { fill: var(--blue); }
  .t-green { fill: var(--green); }
  .t-white { fill: var(--white); }
  .t-ink { fill: var(--ink-blue); }
  .w-regular { font-weight: 400; }
  .w-medium { font-weight: 500; }
  .contact-band { fill: var(--blue); }
</style>
</head>
<body>
<svg class="scene" width="1200" height="1000" viewBox="0 0 1200 1000" role="group" aria-label="Lena Darrow business card, front and back">
  <defs>
    <filter id="card-shadow" x="-5%" y="-5%" width="110%" height="115%">
      <feDropShadow dx="0" dy="3" stdDeviation="4" flood-opacity="0.2"/>
    </filter>
  </defs>

  <!-- Front -->
  <g class="card-front" aria-label="Card front">
    <rect class="card-front-face" x="136" y="100" width="624" height="385" filter="url(#card-shadow)"/>
    <circle class="mark-ring-blue" cx="325" cy="283" r="112"/>
    <text class="mark-name-blue" x="325" y="297" text-anchor="middle" font-size="40" textLength="150" lengthAdjust="spacingAndGlyphs">Vivamora</text>

    <rect class="contact-band" x="142" y="400" width="393" height="32"/>
    <text class="t-white w-medium" x="178" y="426" font-size="25" textLength="114" lengthAdjust="spacingAndGlyphs">0471 552 908</text>
    <text class="t-white w-regular" x="312" y="426" font-size="25" textLength="213" lengthAdjust="spacingAndGlyphs">lena@vivamora.com.au</text>

    <g class="identity" text-anchor="end">
      <text class="t-blue w-regular" x="688" y="180" font-size="82" textLength="116" lengthAdjust="spacingAndGlyphs">Lena</text>
      <text class="t-blue w-medium" x="740" y="255" font-size="90" textLength="190" lengthAdjust="spacingAndGlyphs">Darrow</text>
      <text class="t-green w-regular" x="736" y="290" font-size="40" textLength="201" lengthAdjust="spacingAndGlyphs">Biocentric Coach</text>
      <text class="t-green w-medium" x="740" y="336" font-size="56" textLength="205" lengthAdjust="spacingAndGlyphs">Co-Director</text>
      <text class="t-blue w-regular" x="745" y="374" font-size="42" textLength="205" lengthAdjust="spacingAndGlyphs">Vivamora School</text>
      <text class="t-blue w-medium" x="747" y="418" font-size="54" textLength="207" lengthAdjust="spacingAndGlyphs">of Australia</text>
      <text class="t-green w-medium" x="748" y="460" font-size="44" textLength="208" lengthAdjust="spacingAndGlyphs">vivamora.com.au</text>
    </g>
  </g>

  <!-- Back -->
  <g class="card-back" aria-label="Card back">
    <rect class="card-back-face" x="428" y="512" width="624" height="385" filter="url(#card-shadow)"/>
    <circle class="mark-ring-white" cx="735" cy="582" r="50"/>
    <text class="mark-name-white" x="735" y="589" text-anchor="middle" font-size="22" textLength="74" lengthAdjust="spacingAndGlyphs">Vivamora</text>

    <g class="about t-white w-regular" font-size="34">
      <text x="466" y="682" textLength="552" lengthAdjust="spacingAndGlyphs">The <tspan class="t-ink">Vivamora</tspan> system facilitates the expression of</text>
      <text x="455" y="720" textLength="575" lengthAdjust="spacingAndGlyphs">human potential for health, <tspan class="t-ink">happiness</tspan> and humanity</text>
      <text x="467" y="758" textLength="553" lengthAdjust="spacingAndGlyphs">through <tspan class="t-ink">music</tspan>, movement and group interaction.</text>
      <text x="455" y="815" textLength="575" lengthAdjust="spacingAndGlyphs">It was developed in <tspan class="w-medium">1976</tspan> by <tspan class="t-ink">Emilio Vasca Orduña</tspan>,</text>
      <text x="455" y="853" textLength="575" lengthAdjust="spacingAndGlyphs">a Chilean anthropologist and clinical psychologist</text>
    </g>
  </g>

  <!-- Icon tile -->
  <g class="icon-tile" aria-label="Vivamora icon tile">
    <rect class="tile-face" x="1088" y="97" width="112" height="94"/>
    <circle class="mark-ring-white" cx="1142" cy="143" r="32"/>
    <text class="mark-name-white" x="1142" y="148" text-anchor="middle" font-size="15" textLength="50" lengthAdjust="spacingAndGlyphs">Vivamora</text>
  </g>
</svg>
</body>
</html>
```